Skill Up Salary Up

Full Page
7.5 w x 10 h / 8 w x 10.75 h + .25" bleed
Full-Page Career Course Ad
Project Overview
• Goal: Create a visually attractive, modern, and uncluttered full-page magazine advertisement to list available career courses.
• Tone: Creative, professional, and attention-grabbing to prevent the reader from turning the page. The final design must prioritize readability.

Content Requirements
1. Header/Headline: Must be the primary focus. And grab peoples attention
2. Course Listing: A clear, well-organized list of the career courses.
________________________________________
Design & Aesthetic Directives
1. Layout & Readability (Crucial)
• The final ad must not look crowded or busy.
• Prioritize white space to make the text "breathe" and ensure the course list is easy to scan and read.
• Use a modern, clean, and professional typeface (font choice is critical for the aesthetic).
2. Visual Style
• Aim for a creative, modern, and fresh look. Avoid outdated or generic stock imagery/layouts.
3. Imagery/Graphic Element (Artist's Choice)
You have creative freedom regarding the main graphic element.
• Option A (Photography): Use a photo of a white male American with a collared shirt. The imagery should convey success, focus, or professional development.
• Option B (Vector/Illustration): Use a modern vector graphic, illustration, or abstract design. This could be used to symbolize growth, connection, or a career path.
The choice of graphic element is yours, but it must support the overall modern and uncrowded aesthetic.

Requirements
Must have
• Partial listing .. is part of the Harbor Lantern Course

```html
<!DOCTYPE html>
<html lang="en">
<head>
<meta charset="utf-8">
<title>Skill Up Salary Up – Harbor Lantern Course</title>
<link rel="stylesheet" href="https://fonts.googleapis.com/css2?family=Oswald:wght@500&family=Mulish:wght@700;800&display=swap">
<style>
:root{
  --navy:#1f4796;
  --red:#e4363b;
  --blue-text:#2a5ba8;
  --sky:#3f8fd0;
  --ink:#2b2b2b;
  --panel:#eef2f8;
  --paper:#ffffff;
  --mat:#000000;
}
*{box-sizing:border-box;margin:0;padding:0}
html,body{width:945px;height:1200px;overflow:hidden;background:var(--mat)}
.canvas{position:relative;width:945px;height:1200px;background:var(--mat)}
.page{position:absolute;left:94px;top:95px;width:757px;height:1020px;background:var(--paper);overflow:hidden;font-family:"Mulish",sans-serif;color:var(--ink)}
.hero-photo{position:absolute;left:0;top:0;width:757px;height:399px;
  background:linear-gradient(180deg,#8f9bb4 0%,#c7a99a 38%,#d89a6e 52%,#4a5a78 70%,#25314a 100%)}
.headline{position:absolute;left:0;top:448px;width:757px;text-align:center;font-family:"Mulish",sans-serif;font-weight:800;font-size:54px;line-height:70px;letter-spacing:.5px;color:var(--navy);white-space:nowrap}
.courses-tab{position:absolute;left:269px;top:563px;width:218px;height:28px;background:var(--red);color:#fff;font-weight:800;font-size:16px;text-align:center;line-height:28px;z-index:2}
.courses-panel{position:absolute;left:14px;top:589px;width:730px;height:297px;border:2px solid var(--red);background:var(--panel);display:flex;padding:12px 0 14px}
.course{position:relative;display:flex;flex-direction:column;align-items:center;text-align:center;padding:0 5px}
.course+.course{border-left:1.5px solid var(--red)}
.course.business{width:214px}
.course.software{width:155px}
.course.books{width:128px}
.course.it{width:123px}
.course.office{width:106px}
.course-icon{width:33px;height:33px;flex:none}
.course-title{font-weight:700;font-size:13.5px;line-height:18.5px;margin-top:8px;color:var(--ink)}
.course-tagline{color:var(--blue-text);font-weight:700;font-size:11.3px;line-height:14px;margin-top:3px}
.sub-head{font-family:"Oswald",sans-serif;font-weight:500;font-size:12.5px;margin-top:7px;color:var(--ink)}
.blue-list{list-style:none;color:var(--blue-text);font-weight:700;font-size:9.8px;line-height:12.2px;margin-top:3px;white-space:nowrap}
.dark-list{list-style:none;color:var(--ink);font-weight:700;font-size:10px;line-height:12.6px;margin-top:4px}
.blue-list li::before,.dark-list li::before{content:"• "}
.wrap li{white-space:normal}
.partial{align-self:stretch;display:flex;align-items:center;gap:8px;margin:6px 0 0 4px}
.partial-label{font-family:"Oswald",sans-serif;font-weight:500;font-size:12.5px}
.partial-rule{flex:1;height:1px;background:var(--navy)}
.partial-lists{align-self:stretch;display:flex;text-align:left;padding-left:2px}
.partial-lists ul{width:50%;margin-top:1px}
.optional{margin-top:10px;font-size:9.8px;line-height:12px;font-weight:700}
.optional b{color:var(--blue-text)}
.lab-note{color:var(--blue-text);font-weight:700;font-size:10px;line-height:12.4px;margin-top:7px}
.schedule{position:absolute;bottom:0;left:50%;transform:translateX(-50%);border:1px solid #b9c3d3;background:#fff;color:var(--blue-text);font-weight:700;font-size:9.2px;line-height:12.5px;padding:1px 3px;white-space:nowrap}
.schedule span{display:block;padding:0 1px}
.schedule span+span{border-top:1px solid var(--navy)}
.course.software .schedule{bottom:7px}
.audience{position:absolute;top:893px;left:0;width:757px;text-align:center;font-weight:700;font-size:15.5px;color:#333}
.audience .bar{color:var(--red);margin:0 6px}
.contact-row{position:absolute;top:917px;left:0;width:757px;height:24px}
.contact-row .rule{position:absolute;top:10px;height:2.5px;background:var(--red)}
.contact-row .rule.left{left:0;width:327px}
.contact-row .rule.right{left:430px;width:327px}
.contact-label{position:absolute;left:327px;width:103px;text-align:center;font-weight:700;font-size:15.5px;line-height:22px;color:#222}
</style>
</head>
<body>
<div class="canvas">
  <div class="page">
    <div class="hero-photo" role="img" aria-label="Photo of a smiling businessman in a white collared shirt on a phone call at a laptop, modern glass office towers at sunset behind him"></div>

    <h1 class="headline">SKILL UP SALARY UP</h1>

    <div class="courses-tab">Upcoming HLC Courses</div>

    <section class="courses-panel">
      <article class="course business">
        <svg class="course-icon" viewBox="0 0 33 33"><circle cx="16.5" cy="16.5" r="16" fill="#1f4796"/><circle cx="16.5" cy="16.5" r="14" fill="#3f8fd0"/><path d="M8,22 Q12,19 16.5,22 Q21,19 25,22 L25,24 Q21,21 16.5,24 Q12,21 8,24 Z" fill="#fff"/><circle cx="16.5" cy="13" r="4" fill="none" stroke="#fff" stroke-width="1.5"/></svg>
        <h2 class="course-title">BUSINESS SKILLS &amp;<br>KNOWLEDGE</h2>
        <p class="course-tagline">Impress your interviewer<br>Maximize Income<br>Start / Run Your Business</p>
        <div class="partial"><span class="partial-label">PARTIAL LISTING</span><span class="partial-rule"></span></div>
        <div class="partial-lists">
          <ul class="blue-list"><li>Computers</li><li>Marketing</li><li>Sales</li><li>Finance</li><li>Healthcare</li><li>Business Strategy</li></ul>
          <ul class="blue-list"><li>Communication</li><li>LedgerDesk</li><li>Investments</li><li>Real Estate</li><li>Accounting</li></ul>
        </div>
        <div class="schedule"><span>4-5 MONTHS</span><span>NOV 2025</span></div>
      </article>

      <article class="course software">
        <svg class="course-icon" viewBox="0 0 33 33"><circle cx="16.5" cy="16.5" r="16" fill="#1f4796"/><circle cx="16.5" cy="16.5" r="14" fill="#3f8fd0"/><rect x="9" y="11" width="15" height="10" rx="1" fill="none" stroke="#fff" stroke-width="1.5"/><rect x="13" y="22" width="7" height="1.5" fill="#fff"/></svg>
        <h2 class="course-title">SOFTWARE, WEB<br>&amp; APPS</h2>
        <p class="course-tagline">#2 Best Tech Job<br>National Careers<br>Review 2025</p>
        <h3 class="sub-head">Job Opportunities</h3>
        <ul class="blue-list" style="text-align:left;font-size:9.4px;line-height:13px"><li>Computer Programmer</li><li>Software Developer/Mobile</li><li>Engineer Developer (Apps</li></ul>
        <p class="optional"><b>OPTIONAL:</b><br>Bachelors in Prog. &amp; Tech.</p>
        <div class="schedule"><span>NOV 2025</span></div>
      </article>

      <article class="course books">
        <svg class="course-icon" viewBox="0 0 33 33"><circle cx="16.5" cy="16.5" r="16" fill="#1f4796"/><circle cx="16.5" cy="16.5" r="14" fill="#3f8fd0"/><rect x="9" y="11" width="8" height="11" rx="1" fill="#fff"/><rect x="19" y="11" width="6" height="11" rx="1" fill="none" stroke="#fff" stroke-width="1.3"/></svg>
        <h2 class="course-title">BOOKKEEPING<br>LEDGERDESK</h2>
        <p class="course-tagline">Train for a quality<br>job Manage your<br>own books</p>
        <ul class="blue-list wrap" style="margin-top:12px"><li>Finance<br>Management</li><li style="margin-top:3px">Customer &amp; Vendor<br>Mgmt.</li><li style="margin-top:3px">Advanced Tools</li></ul>
        <div class="schedule"><span>5 WEEKS</span><span>NOV 2025</span></div>
      </article>

      <article class="course it">
        <svg class="course-icon" viewBox="0 0 33 33"><circle cx="16.5" cy="16.5" r="16" fill="#1f4796"/><circle cx="16.5" cy="16.5" r="14" fill="#3f8fd0"/><rect x="11" y="9" width="11" height="8" fill="none" stroke="#fff" stroke-width="1.4"/><path d="M16.5,17 V21 M10,21 H23 M10,21 V24 M23,21 V24" stroke="#fff" stroke-width="1.4" fill="none"/></svg>
        <h2 class="course-title">IT DESKTOP &amp;<br>NETWORKING<br>SUPPORT</h2>
        <p class="course-tagline" style="margin-top:0">#2 Best Tech Job<br>National Careers<br>Review 2025</p>
        <h3 class="sub-head">MASTERS IT:</h3>
        <ul class="blue-list" style="line-height:14px"><li>Panes OS</li><li>Networks</li><li>Servers</li><li>Cloud</li></ul>
        <div class="schedule"><span>7 MONTHS</span><span>DEC 2025</span></div>
      </article>

      <article class="course office">
        <svg class="course-icon" viewBox="0 0 33 33"><circle cx="16.5" cy="16.5" r="16" fill="#1f4796"/><circle cx="16.5" cy="16.5" r="14" fill="#3f8fd0"/><rect x="9" y="15" width="15" height="9" rx="1" fill="none" stroke="#fff" stroke-width="1.4"/><rect x="10" y="8" width="4" height="4" fill="#fff"/><rect x="15" y="8" width="4" height="4" fill="#fff"/><rect x="20" y="8" width="4" height="4" fill="#fff"/></svg>
        <h2 class="course-title">ORBIT<br>OFFICE-<br>COMPUTERS</h2>
        <p class="course-tagline">The New Job<br>Prerequisite</p>
        <ul class="dark-list"><li>Gridwork</li><li>Scribe Pad</li><li>Mailroom</li><li>SlideDeck</li></ul>
        <p class="lab-note">Computer lab<br>available<br>to practice</p>
        <div class="schedule"><span>5 WEEKS</span><span>DEC 2025</span></div>
      </article>
    </section>

    <p class="audience">MEN &amp; WOMEN<span class="bar">|</span>IN-PERSON &amp; REMOTE<span class="bar">|</span>PARTIAL SCHOLORASHIPS</p>
    <div class="contact-row">
      <span class="rule left"></span>
      <span class="contact-label">Contact</span>
      <span class="rule right"></span>
    </div>
  </div>
</div>
</body>
</html>
```